New Business Card for Web Design/Internet Marketing Company

Looking for a great looking new business card. We are a 10 year old web design, internet marketing and website management company that works mostly with small businesses.

Our new card needs to better match the colors and style of our website, be bold, extremely usable and slightly edgy.

Target Market(s)

Small/Medium businesses that have websites

Industry/Entity Type

Internet

Requirements
Must have
• Front and back design, full color, rounded corners please

Must use the colors/style of our website (JPG provided)

INFO FOR CARDS (as readable as possible please)
Mark Pellow
President/CEO
mark@brightlanesites.com
Phone: 520-481-7093
Toll Free: 866-481-7093
Address: 4315 E. Kestrel Ave. Ste. 140, Tucson, AZ 85733

THINGS I WANT TO PROMOTE (if there is room):
1. Our Website - www.brightlanesites.com

2. Social Media
Twitter: @brightlanesites
Facebook: www.facebook.com/brightlanesites

3. Our Services
Web Design
Internet Marketing
Website Management

```html
<!DOCTYPE html>
<html lang="en">
<head>
<meta charset="utf-8">
<title>Bright Lane Sites – Business Card</title>
<link rel="stylesheet" href="https://fonts.googleapis.com/css2?family=Arimo:ital,wght@0,400;0,700;1,700&display=swap">
<style>
  :root {
    --backdrop: #9a7656;
    --navy-deep: #1c2433;
    --navy-glow: #0a3a70;
    --orange: #f0842c;
    --sky: #2a8fd0;
    --sky-soft: #4aa6d8;
    --white: #ffffff;
    --ink-light: #e9eef5;
  }
  * { margin: 0; padding: 0; box-sizing: border-box; }
  html, body { width: 1200px; height: 1125px; overflow: hidden; }
  body {
    background: var(--backdrop);
    font-family: "Arimo", Arial, sans-serif;
    position: relative;
  }
  .card {
    position: absolute;
    left: 158px;
    width: 760px;
    height: 491px;
    border-radius: 42px;
    overflow: hidden;
    box-shadow: 0 2px 8px rgba(0,0,0,0.35);
  }
  .card--front { top: 55px; }
  .card--back { top: 583px; background: var(--white); }
  .dark-field {
    position: absolute;
    top: 0; left: 0; height: 100%;
    background: radial-gradient(ellipse at 50% 45%, var(--navy-glow) 0%, #0d2b52 40%, var(--navy-deep) 80%);
  }
  .card--front .dark-field { width: 100%; }
  .card--back .dark-field { width: 402px; }
  .centered { position: absolute; width: 100%; text-align: center; }
  .brand-name {
    color: var(--orange);
    font-weight: 700;
    letter-spacing: -1px;
    white-space: nowrap;
  }
  .tagline { color: var(--white); font-weight: 400; }
  .card--front .brand-name { top: 225px; font-size: 66px; }
  .card--front .tagline { top: 312px; font-size: 24px; }
  .web-address {
    top: 400px; color: var(--white);
    font-size: 28px; font-weight: 700; font-style: italic;
  }
  .social {
    top: 437px; color: var(--ink-light); font-size: 13px; line-height: 16px;
  }
  .social-line { display: flex; justify-content: center; align-items: center; gap: 6px; }
  .social-mark { width: 12px; height: 12px; border-radius: 2px; background: var(--sky); display: inline-block; }

  .card--back .centered { width: 402px; }
  .card--back .brand-name { top: 170px; font-size: 46px; }
  .card--back .tagline { top: 234px; font-size: 22px; }
  .services {
    top: 286px; color: var(--white); font-size: 19px; line-height: 21.5px;
  }
  .address {
    position: absolute; left: 43px; top: 410px;
    color: var(--orange); font-size: 19px; line-height: 22px;
  }
  .contact-side {
    position: absolute; left: 402px; top: 0; width: 358px; height: 100%;
    text-align: center;
  }
  .person-name {
    position: absolute; top: 108px; width: 100%;
    color: var(--sky-soft); font-size: 35px; font-weight: 700;
  }
  .person-title {
    position: absolute; top: 145px; width: 100%;
    color: var(--sky-soft); font-size: 15px; font-weight: 700;
  }
  .email {
    position: absolute; top: 338px; width: 100%;
    color: var(--orange); font-size: 23px;
  }
  .phones { position: absolute; top: 380px; left: 92px; }
  .phone-line {
    display: flex; align-items: center; gap: 2px; height: 31px;
    color: var(--sky); font-size: 23px; font-weight: 700;
  }
  .phone-icon { width: 30px; height: 30px; }
</style>
</head>
<body>

<section class="card card--front">
  <div class="dark-field"></div>
  <div class="centered brand-name">Bright Lane Sites</div>
  <div class="centered tagline">Love your Website</div>
  <div class="centered web-address">www.brightlanesites.com</div>
  <div class="centered social">
    <div class="social-line"><span class="social-mark"></span>www.friendlane.net/brightlanesites</div>
    <div class="social-line"><span class="social-mark"></span>@brightlanesites</div>
  </div>
</section>

<section class="card card--back">
  <div class="dark-field"></div>
  <div class="centered brand-name">Bright Lane Sites</div>
  <div class="centered tagline">Love your Website</div>
  <div class="centered services">
    <div>Internet Marketing</div>
    <div>Web Design</div>
    <div>Website Management</div>
  </div>
  <div class="address">
    <div>4315 E. Kestrel Ave. Ste. 140,</div>
    <div>Tucson, AZ 85733</div>
  </div>

  <div class="contact-side">
    <div class="person-name">Mark Pellow</div>
    <div class="person-title">President/CEO</div>
    <div class="email">mark@brightlanesites.com</div>
    <div class="phones">
      <div class="phone-line">
        <svg class="phone-icon" viewBox="0 0 30 30" aria-hidden="true">
          <circle cx="15" cy="15" r="13" fill="none" stroke="#f0842c" stroke-width="2"/>
          <path d="M11 8 q-4 7 3 14 l3 -2 -3 -4 -2 1 q-2 -3 0 -6 l2 1 1 -4 z" fill="#f0842c"/>
        </svg>
        <span>520-481-7093</span>
      </div>
      <div class="phone-line">
        <svg class="phone-icon" viewBox="0 0 30 30" aria-hidden="true">
          <circle cx="15" cy="15" r="13" fill="none" stroke="#f0842c" stroke-width="2"/>
          <path d="M11 8 q-4 7 3 14 l3 -2 -3 -4 -2 1 q-2 -3 0 -6 l2 1 1 -4 z" fill="#f0842c"/>
        </svg>
        <span>866-481-7093</span>
      </div>
    </div>
  </div>
</section>

</body>
</html>
```